VFX Company Business Card Design Project

The Pixel Harbor is a decentralized Visual Effects Studio servicing the television and feature film industries.
Project Brief:
Take our logo that was previously designed on Sketch Forum and make a double sided business card.
Requirements:
- Card MUST be double sided.
- Front of card MUST have the yellow part of our logo against the dark grey background.
- Back of card is completely up to the designer.
- Back of card must include the complete company logo.
Please follow these File Preparation guidelines:
http://printmarlow.example/infopage?file=filetype_en&s=PrintMarlow_new&lang=en
Industry/Entity Type
Business
Look and feel
Each slider illustrates characteristics of the customer's brand and the style your logo design should communicate.

```html
<!DOCTYPE html>
<html lang="en">
<head>
<meta charset="utf-8">
<title>The Pixel Harbor – Business Card</title>
<link href="https://fonts.googleapis.com/css2?family=Oswald:wght@500&family=Roboto+Condensed:wght@400&display=swap" rel="stylesheet">
<style>
  :root {
    --backdrop: #d9d9d9;
    --card: #2a2a2b;
    --card-edge: #343436;
    --accent: #f2c12e;
    --logo-grey: #9aa1a3;
    --name-white: #f4f4f4;
    --surname-grey: #8f999b;
    --text: #e6e6e6;
    --icon-bg: #d8d8d8;
    --icon-fg: #2a2a2b;
  }
  * { box-sizing: border-box; margin: 0; padding: 0; }
  html, body { width: 1200px; height: 861px; overflow: hidden; }
  body {
    background: var(--backdrop);
    position: relative;
    font-family: "Roboto Condensed", "Arial Narrow", sans-serif;
  }
  .card {
    position: absolute;
    top: 280px;
    width: 525px;
    height: 300px;
    border-radius: 16px;
    background: linear-gradient(160deg, var(--card-edge), var(--card) 60%);
    box-shadow: 0 10px 30px rgba(0,0,0,.25);
    overflow: hidden;
  }
  .card--front { left: 50px; }
  .card--back { left: 625px; }

  .brand {
    display: flex;
    align-items: center;
    gap: 10px;
  }
  .brand__dot {
    width: 26px; height: 26px; border-radius: 50%;
    background: var(--accent);
    flex: none;
  }
  .brand__name {
    font-family: "Oswald", sans-serif;
    font-weight: 500;
    color: var(--logo-grey);
    font-size: 24px;
    line-height: 1.2;
    letter-spacing: .5px;
    white-space: nowrap;
  }

  /* front */
  .front-band {
    position: absolute;
    left: 0; right: 0; top: 150px;
    transform: translateY(-50%);
    display: flex;
    align-items: center;
  }
  .rule { height: 3px; background: var(--accent); }
  .front-band .rule--left { width: 118px; margin-right: 14px; }
  .front-band .rule--right { flex: 1; margin-left: 14px; }

  /* back */
  .back-rule-top { position: absolute; left: 22px; top: 0; width: 3px; height: 106px; background: var(--accent); }
  .back-rule-bottom { position: absolute; left: 22px; bottom: 0; width: 3px; height: 24px; background: var(--accent); }
  .back-brand {
    position: absolute; top: 48px; right: 0; left: 235px;
    display: flex; align-items: center;
  }
  .back-brand .rule { flex: 1; margin-left: 12px; }
  .identity { position: absolute; left: 22px; top: 112px; }
  .identity__name {
    font-family: "Oswald", sans-serif;
    font-weight: 500;
    font-size: 30px;
    line-height: 1.1;
    color: var(--name-white);
    text-transform: uppercase;
    white-space: nowrap;
  }
  .identity__name span { color: var(--surname-grey); }
  .identity__role { font-size: 14px; line-height: 1.2; color: var(--text); margin-top: 2px; text-transform: uppercase; }

  .contacts {
    position: absolute; left: 22px; top: 182px; right: 20px;
    display: grid;
    grid-template-columns: 212px 1fr;
    row-gap: 6px;
    font-size: 14px;
    line-height: 1.2;
    color: var(--text);
  }
  .contact { display: flex; align-items: center; gap: 8px; white-space: nowrap; height: 24px; }
  .contact--wide { grid-column: 1 / -1; }
  .contact svg { width: 24px; height: 24px; flex: none; }
</style>
</head>
<body>

<section class="card card--front" aria-label="Card front">
  <div class="front-band">
    <div class="rule rule--left"></div>
    <div class="brand">
      <div class="brand__dot"></div>
      <div class="brand__name">THE PIXEL HARBOR</div>
    </div>
    <div class="rule rule--right"></div>
  </div>
</section>

<section class="card card--back" aria-label="Card back">
  <div class="back-rule-top"></div>
  <div class="back-rule-bottom"></div>

  <div class="back-brand">
    <div class="brand">
      <div class="brand__dot"></div>
      <div class="brand__name">THE PIXEL HARBOR</div>
    </div>
    <div class="rule"></div>
  </div>

  <div class="identity">
    <div class="identity__name">Name <span>Surname</span></div>
    <div class="identity__role">Position</div>
  </div>

  <div class="contacts">
    <div class="contact contact--wide">
      <svg viewBox="0 0 26 26" aria-hidden="true"><circle cx="13" cy="13" r="13" fill="var(--icon-bg)"/><rect x="8" y="7" width="10" height="13" fill="var(--icon-fg)"/><rect x="10" y="9" width="2" height="2" fill="var(--icon-bg)"/><rect x="14" y="9" width="2" height="2" fill="var(--icon-bg)"/><rect x="10" y="13" width="2" height="2" fill="var(--icon-bg)"/><rect x="14" y="13" width="2" height="2" fill="var(--icon-bg)"/></svg>
      1234 Lorem Road, Ipsum City, NY 5678
    </div>
    <div class="contact">
      <svg viewBox="0 0 26 26" aria-hidden="true"><circle cx="13" cy="13" r="13" fill="var(--icon-bg)"/><path d="M8 17 L11 14 M15 12 L18 9" stroke="var(--icon-fg)" stroke-width="4" stroke-linecap="round"/><path d="M10 16 L16 10" stroke="var(--icon-fg)" stroke-width="2"/></svg>
      123-456-789
    </div>
    <div class="contact">
      <svg viewBox="0 0 26 26" aria-hidden="true"><circle cx="13" cy="13" r="13" fill="var(--icon-bg)"/><rect x="9.5" y="6" width="7" height="14" rx="1.5" fill="var(--icon-fg)"/><rect x="11" y="8" width="4" height="5" fill="var(--icon-bg)"/></svg>
      123-456-789
    </div>
    <div class="contact">
      <svg viewBox="0 0 26 26" aria-hidden="true"><circle cx="13" cy="13" r="13" fill="var(--icon-bg)"/><rect x="7" y="9" width="12" height="8" fill="var(--icon-fg)"/><path d="M7 9 L13 14 L19 9" stroke="var(--icon-bg)" stroke-width="1.2" fill="none"/></svg>
      email@yourdomain.com
    </div>
    <div class="contact">
      <svg viewBox="0 0 26 26" aria-hidden="true"><circle cx="13" cy="13" r="13" fill="var(--icon-bg)"/><rect x="7" y="8" width="12" height="8" fill="var(--icon-fg)"/><rect x="8.5" y="9.5" width="9" height="5" fill="var(--icon-bg)"/><rect x="10" y="17" width="6" height="2" fill="var(--icon-fg)"/></svg>
      www.yourdomain.com
    </div>
  </div>
</section>

</body>
</html>
```